b2c portal. ZippyGrub. Attract diners and drinkers to restaurant/bar deals

aggregator site for restaurants and bars to promote their deals/discounts

1. we are an aggregator portal that lists all deals and discounts (Happy Hour, etc.) for restaurants and bars. the layout is similar to Kivo and RoamScout, without the ratings.
2. the target market is identical to Kivo and those searching for restaurants on RoamScout.
3. I have attached a file of a preliminary screenshot of a home page.

Target Market(s)

all guests of restaurants and bars

Number of Pages Required

4 page

Requirements
Must have
• a good story loop.
see Kivo, RoamScout, DashMeals
Should not have
• keep it simple

```html
<!DOCTYPE html>
<html lang="en">
<head>
<meta charset="utf-8">
<title>ZippyGrub – Find Restaurant Offers</title>
<link rel="stylesheet" href="https://fonts.googleapis.com/css2?family=Catamaran:wght@400;500;600;700;800&family=Alegreya:ital@1&family=Poppins:wght@400;500;600&display=swap">
<style>
:root{
  --teal:#33807c;
  --ink:#1f1f1f;
  --text:#3a3a3a;
  --muted:#5d5d5d;
  --orange:#d0661d;
  --page:#ffffff;
  --header:#f4f4f4;
  --footer:#3d3d3d;
  --footer-text:#d6d6d6;
  --card-shadow:0 2px 10px rgba(0,0,0,.08);
}
*{box-sizing:border-box;margin:0;padding:0}
html,body{width:1200px;height:2970px;overflow:hidden}
body{position:relative;background:var(--page);font-family:"Catamaran",sans-serif;color:var(--text)}
.abs{position:absolute}

/* header */
.site-header{position:absolute;left:0;top:0;width:1200px;height:89px;background:var(--header)}
.nav-cat{position:absolute;top:12px;display:flex;flex-direction:column;align-items:center;font-size:19px;color:var(--ink);font-weight:500}
.nav-cat svg{margin-bottom:4px}
.nav-divider{position:absolute;left:291px;top:22px;width:1px;height:50px;background:#bdbdbd}
.btn{position:absolute;top:26px;height:38px;width:96px;border-radius:3px;font-family:"Poppins",sans-serif;font-size:14px;display:flex;align-items:center;justify-content:center}
.btn-outline{left:879px;border:1px solid #9a9a9a;color:var(--ink);background:#fff}
.btn-solid{left:985px;background:var(--teal);color:#fff}

/* hero */
.hero{position:absolute;left:0;top:89px;width:1200px;height:603px;background:linear-gradient(180deg,#5a6470 0%,#6b4a33 40%,#3e2c22 75%,#1f2228 100%)}
.hero-links{position:absolute;right:120px;top:18px;display:flex;align-items:center;gap:22px;color:#fff;font-size:20px;font-weight:500}
.hero-links span.sep{width:1px;height:22px;background:#fff;opacity:.7}
.brand-hero{position:absolute;left:0;width:1200px;top:130px;text-align:center;color:#fff;font-weight:800;font-size:62px;letter-spacing:-1px}
.hero-title{position:absolute;left:0;width:1200px;top:205px;text-align:center;color:#fff;font-family:"Alegreya",serif;font-style:italic;font-size:58px}
.hero-sub{position:absolute;left:0;width:1200px;top:285px;text-align:center;color:#fff;font-family:"Alegreya",serif;font-style:italic;font-size:28px}
.search{position:absolute;left:326px;top:368px;width:549px;height:41px;background:#fff;border-radius:21px;display:flex;overflow:hidden}
.search .field{flex:1;padding-left:26px;display:flex;align-items:center;font-size:17px;color:#777}
.search .field + .field{border-left:1px solid #ccc;padding-left:14px}
.search .go{width:60px;background:#111;display:flex;align-items:center;justify-content:center;border-radius:0 21px 21px 0}

/* sections */
.section-title{position:absolute;left:0;width:1200px;text-align:center;font-size:40px;font-weight:500;color:var(--ink);letter-spacing:-1.5px}
.cat-card{position:absolute;top:854px;width:245px;height:244px;background:#fff;box-shadow:var(--card-shadow)}
.cat-card .photo{height:184px}
.cat-card .label{text-align:center;font-size:20px;color:var(--ink);padding-top:16px}
.dots{position:absolute;left:572px;top:1131px;display:flex;align-items:center;gap:9px}
.dot{width:10px;height:10px;border-radius:50%;border:1px solid #777}
.dot.on{width:15px;height:15px;border:none;background:var(--teal)}

.venue{position:absolute;width:277px;height:340px;background:#fff;box-shadow:var(--card-shadow)}
.venue .photo{position:absolute;left:8px;top:8px;width:261px;height:185px}
.venue .fav{position:absolute;right:13px;top:13px;width:28px;height:28px;border-radius:50%;background:#1e1e1e;display:flex;align-items:center;justify-content:center}
.venue h3{position:absolute;left:16px;top:208px;font-size:18px;font-weight:500;color:var(--ink)}
.venue p{position:absolute;left:16px;top:240px;width:240px;font-size:15px;line-height:19px;color:var(--muted)}
.venue .age{position:absolute;left:18px;top:297px;font-size:14px;color:var(--orange)}

.post{position:absolute;top:2165px;width:278px}
.post .photo{height:175px;border-radius:4px;position:relative}
.post .date{position:absolute;left:8px;top:8px;width:46px;height:46px;border-radius:50%;background:#fff;font-size:11px;font-weight:700;line-height:11px;color:var(--ink);display:flex;flex-direction:column;align-items:center;justify-content:center}
.post .meta{margin-top:18px;font-size:13px;color:var(--teal)}
.post .meta span{margin-left:14px}
.post h4{margin-top:4px;font-size:20px;line-height:24px;font-weight:500;color:var(--ink)}
.post p{margin-top:10px;font-size:15px;line-height:23px;color:var(--muted)}
.post a{display:inline-block;margin-top:8px;font-size:15px;color:var(--orange);text-decoration:underline}

/* footer */
.site-footer{position:absolute;left:0;top:2605px;width:1200px;height:365px;background:var(--footer);font-family:"Poppins",sans-serif;color:var(--footer-text)}
.f-brand{position:absolute;left:120px;top:138px;font-family:"Catamaran",sans-serif;font-weight:800;font-size:46px;color:#fff;letter-spacing:-1px}
.f-social{position:absolute;left:150px;top:235px;display:flex;gap:14px}
.f-social span{width:16px;height:16px;border-radius:50%;background:#fff}
.f-col h5{font-size:15px;font-weight:600;color:#fff;margin-bottom:14px}
.contact-row{display:flex;gap:12px;font-size:13px;line-height:20px;margin-bottom:14px}
.f-links{list-style:none;font-size:13px;line-height:22.5px}
.f-help p{font-size:14px;line-height:22px;margin-bottom:22px}
.cta{display:inline-flex;align-items:center;gap:10px;background:var(--teal);color:#fff;font-size:18px;padding:10px 22px;border-radius:2px}
.f-rule{position:absolute;left:0;top:298px;width:1200px;height:1px;background:#555}
.f-bottom{position:absolute;top:322px;font-size:15px}
</style>
</head>
<body>

<header class="site-header">
  <div class="nav-cat" style="left:118px">
    <svg width="34" height="32" viewBox="0 0 34 32" fill="none" stroke="#333" stroke-width="1.5"><path d="M9 4h7l-1 10a3 3 0 0 1-5 0z M12.5 15v12 M8 27h9"/><path d="M18 4h7l-1 10a3 3 0 0 1-5 0z M21.5 15v12 M17 27h9"/></svg>
    Diners &amp; Drinkers
  </div>
  <div class="nav-divider"></div>
  <div class="nav-cat" style="left:315px">
    <svg width="34" height="32" viewBox="0 0 34 32" fill="none" stroke="#333" stroke-width="1.5"><circle cx="17" cy="6" r="2"/><path d="M5 20a12 12 0 0 1 24 0z M3 23h28"/></svg>
    Restaurant/Bar
  </div>
  <div class="btn btn-outline">Sign In</div>
  <div class="btn btn-solid">Sign In</div>
</header>

<section class="hero" role="img" aria-label="Photo of a crowd of friends drinking at an outdoor bar under bunting">
  <nav class="hero-links"><span>Blog</span><span class="sep"></span><span>Contact</span></nav>
  <div class="brand-hero">ZIPPYGRUB</div>
  <h1 class="hero-title">Find Restaurant Offers</h1>
  <p class="hero-sub">Your adventure with affordable taste</p>
  <div class="search">
    <div class="field">Were To</div>
    <div class="field">Restaurant/Bar Name</div>
    <div class="go"><svg width="20" height="20" viewBox="0 0 20 20" fill="none" stroke="#fff" stroke-width="2"><circle cx="8" cy="8" r="6"/><path d="M13 13l5 5"/></svg></div>
  </div>
</section>

<h2 class="section-title" style="top:765px">Find the Best Businesses in Town</h2>
<div class="cat-card" style="left:217px"><div class="photo" role="img" aria-label="Friends laughing over dinner" style="background:linear-gradient(135deg,#6a5a4e,#b08a6a,#3d3029)"></div><div class="label">Restaurant</div></div>
<div class="cat-card" style="left:478px"><div class="photo" role="img" aria-label="Group dining at a long candlelit table" style="background:linear-gradient(135deg,#3a2a1e,#7a5a38,#1e1712)"></div><div class="label">Diners &amp; Drinkers</div></div>
<div class="cat-card" style="left:739px"><div class="photo" role="img" aria-label="Warmly lit restaurant interior" style="background:linear-gradient(135deg,#c7b8a4,#a6683a,#4a2a16)"></div><div class="label">Restaurant/Bar</div></div>
<div class="dots"><span class="dot"></span><span class="dot on"></span><span class="dot"></span></div>

<h2 class="section-title" style="top:1212px">Find the Best Restaurant in Town</h2>

<article class="venue" style="left:161px;top:1290px"><div class="photo" role="img" aria-label="Couple sharing a meal" style="background:linear-gradient(135deg,#5e4a3a,#8d7660,#3b2f27)"></div><div class="fav"><svg width="16" height="14" viewBox="0 0 16 14" fill="none" stroke="#fff" stroke-width="1.5"><path d="M8 13L2 7a3.3 3.3 0 0 1 6-4 3.3 3.3 0 0 1 6 4z"/></svg></div><h3>Restaurant Name</h3><p>Lorem Ipsum is simply dummy text of the printing and typesetting</p><span class="age">Opened 4 weeks ago</span></article>
<article class="venue" style="left:462px;top:1290px"><div class="photo" role="img" aria-label="Woman eating a burger with a friend" style="background:linear-gradient(135deg,#6b4a30,#4a6a8a,#2e2a28)"></div><div class="fav"><svg width="16" height="14" viewBox="0 0 16 14" fill="none" stroke="#fff" stroke-width="1.5"><path d="M8 13L2 7a3.3 3.3 0 0 1 6-4 3.3 3.3 0 0 1 6 4z"/></svg></div><h3>Restaurant Name</h3><p>Lorem Ipsum is simply dummy text of the printing and typesetting</p><span class="age">Opened 4 weeks ago</span></article>
<article class="venue" style="left:763px;top:1290px"><div class="photo" role="img" aria-label="Waiter serving a table of friends" style="background:linear-gradient(135deg,#8a8a86,#d8d4cc,#5a544c)"></div><div class="fav"><svg width="16" height="14" viewBox="0 0 16 14" fill="none" stroke="#fff" stroke-width="1.5"><path d="M8 13L2 7a3.3 3.3 0 0 1 6-4 3.3 3.3 0 0 1 6 4z"/></svg></div><h3>Restaurant Name</h3><p>Lorem Ipsum is simply dummy text of the printing and typesetting</p><span class="age">Opened 4 weeks ago</span></article>
<article class="venue" style="left:161px;top:1655px"><div class="photo" role="img" aria-label="Couple sharing a meal" style="background:linear-gradient(135deg,#5e4a3a,#8d7660,#3b2f27)"></div><div class="fav"><svg width="16" height="14" viewBox="0 0 16 14" fill="none" stroke="#fff" stroke-width="1.5"><path d="M8 13L2 7a3.3 3.3 0 0 1 6-4 3.3 3.3 0 0 1 6 4z"/></svg></div><h3>Restaurant Name</h3><p>Lorem Ipsum is simply dummy text of the printing and typesetting</p><span class="age">Opened 4 weeks ago</span></article>
<article class="venue" style="left:462px;top:1655px"><div class="photo" role="img" aria-label="Table set with glasses and a plated dish" style="background:linear-gradient(135deg,#c9953a,#efe2c4,#9a7a58)"></div><div class="fav"><svg width="16" height="14" viewBox="0 0 16 14" fill="none" stroke="#fff" stroke-width="1.5"><path d="M8 13L2 7a3.3 3.3 0 0 1 6-4 3.3 3.3 0 0 1 6 4z"/></svg></div><h3>Restaurant Name</h3><p>Lorem Ipsum is simply dummy text of the printing and typesetting</p><span class="age">Opened 4 weeks ago</span></article>
<article class="venue" style="left:763px;top:1655px"><div class="photo" role="img" aria-label="Couple sharing a meal" style="background:linear-gradient(135deg,#5e4a3a,#8d7660,#3b2f27)"></div><div class="fav"><svg width="16" height="14" viewBox="0 0 16 14" fill="none" stroke="#fff" stroke-width="1.5"><path d="M8 13L2 7a3.3 3.3 0 0 1 6-4 3.3 3.3 0 0 1 6 4z"/></svg></div><h3>Restaurant Name</h3><p>Lorem Ipsum is simply dummy text of the printing and typesetting</p><span class="age">Opened 4 weeks ago</span></article>

<h2 class="section-title" style="top:2080px">Latest Blog</h2>

<article class="post" style="left:159px"><div class="photo" role="img" aria-label="Dinner table with wine glasses and bread" style="background:linear-gradient(135deg,#c9953a,#efe2c4,#8a6a4a)"><div class="date">30<span>Nov</span></div></div><div class="meta">By Admin &nbsp;. <span>2 Comments</span></div><h4>Lorem Ipsum is simply dummy text of the printing</h4><p>There are many variations of passages of available but majority have alteration</p><a>Read More</a></article>
<article class="post" style="left:461px"><div class="photo" role="img" aria-label="Hands sharing salad bowls on a wooden table" style="background:linear-gradient(135deg,#4a3a2e,#8a6a4a,#c8b89a)"><div class="date">30<span>Nov</span></div></div><div class="meta">By Admin &nbsp;. <span>2 Comments</span></div><h4>Lorem Ipsum is simply dummy text of the printing</h4><p>There are many variations of passages of available but majority have alteration</p><a>Read More</a></article>
<article class="post" style="left:764px"><div class="photo" role="img" aria-label="Menu board with cutlery and vegetables on wood" style="background:linear-gradient(135deg,#5a4634,#2a3a44,#7a4a34)"><div class="date">30<span>Nov</span></div></div><div class="meta">By Admin &nbsp;. <span>2 Comments</span></div><h4>Lorem Ipsum is simply dummy text of the printing</h4><p>There are many variations of passages of available but majority have alteration</p><a>Read More</a></article>

<footer class="site-footer">
  <div class="f-brand">ZippyGrub</div>
  <div class="f-social"><span></span><span></span><span></span></div>

  <div class="f-col abs" style="left:350px;top:92px">
    <h5>Contact Us</h5>
    <div class="contact-row"><svg width="16" height="18" viewBox="0 0 16 18" fill="none" stroke="#ddd" stroke-width="1.4"><path d="M8 17s6-6 6-10A6 6 0 0 0 2 7c0 4 6 10 6 10z"/><circle cx="8" cy="7" r="2"/></svg><span>42 Lantern Row #B<br>Millbrook 20481</span></div>
    <div class="contact-row"><svg width="18" height="18" viewBox="0 0 18 18" fill="#ddd"><path d="M4 1l3 4-2 2c1 2 3 4 5 5l2-2 4 3-2 3C8 16 2 10 1 4z"/></svg><span>(555) 014-2290</span></div>
    <div class="contact-row"><svg width="18" height="14" viewBox="0 0 18 14" fill="#ddd"><path d="M1 1h16v12H1z"/><path d="M1 1l8 7 8-7" stroke="#3d3d3d" stroke-width="1.4" fill="none"/></svg><span>hello@zippygrub.example</span></div>
  </div>

  <div class="f-col abs" style="left:616px;top:92px">
    <h5>Company</h5>
    <ul class="f-links"><li>Home</li><li>Diners &amp; Drinkers</li><li>Restaurant/Bar</li><li>Services</li><li>Blog</li><li>Contact Us</li></ul>
  </div>

  <div class="f-col f-help abs" style="left:804px;top:92px;width:280px">
    <h5>Stil have questions?</h5>
    <p>Contact us usig this form. A repesenta-tive will aswer your questions as soon as possible.</p>
    <span class="cta">Get In Touch <svg width="22" height="12" viewBox="0 0 22 12" fill="none" stroke="#fff" stroke-width="1.6"><path d="M1 6h19M15 1l5 5-5 5"/></svg></span>
  </div>

  <div class="f-rule"></div>
  <div class="f-bottom" style="left:120px">Copyright 2020 ZippyGrub. All Rights Reserved.</div>
  <div class="f-bottom" style="left:837px;font-size:13px">Privacy Policy</div>
  <div class="f-bottom" style="left:953px;font-size:13px">Terms Of Services</div>
</footer>

</body>
</html>
```